Bref créative
Business Card, Stationary, and #10 Envelope
Bright Harbor Advising
I need double sided standard sized Business Card [3.5" x 2"]
Logo font was Brussels, please use the same, similar or compatible font
Professional
Milo Trenholt
Certified College Planning Specialist
4870 Quarlow Lane
Pellham Ridge, Idaho 58246
milo@brightharboradvising.example
www.brightharboradvising.example
Would like the colors of the card to match the logo. Gold/yellow, black, and white. 2 designs are included, one with a gold tag line, and one with a black tag line. I prefer the gold tag line so I am hoping your designs can utilize that coloring but I am open to ideas.
We can help you:
-Afford college while protecting retirement
-Lower the total cost of college
-Maximize financial aid qualification
-Compare the net cost of public vs private schools
Logo
Logo 2

```html
<!DOCTYPE html>
<html lang="en">
<head>
<meta charset="utf-8">
<title>Bright Harbor Advising — Business Card</title>
<link rel="stylesheet" href="https://fonts.googleapis.com/css2?family=Cabin:ital,wght@0,500;0,600;1,700&family=Libre+Baskerville:wght@400;700&display=swap">
<style>
  :root {
    --page: #d9d9d9;
    --ink: #0c0c0c;
    --paper: #ffffff;
    --band: #ececec;
    --gold: #e4a816;
    --gold-soft: #f0c24a;
    --text-dark: #1d1d1d;
    --text-light: #f2f2f2;
  }
  * { box-sizing: border-box; margin: 0; padding: 0; }
  html, body { width: 1200px; height: 1000px; overflow: hidden; }
  body {
    background: var(--page);
    position: relative;
    font-family: "Libre Baskerville", Georgia, serif;
  }
  .card {
    position: absolute;
    left: 200px;
    width: 800px;
    height: 457px;
    overflow: hidden;
    box-shadow: 0 6px 18px rgba(0,0,0,.25);
  }
  .card svg.card__art { position: absolute; inset: 0; }
  .card--services { top: 28px; background: var(--ink); }
  .card--contact { top: 515px; background: var(--paper); }

  .services {
    position: absolute;
    left: 0; right: 0; top: 150px;
    text-align: center;
    color: var(--text-dark);
    font-size: 17px;
    line-height: 29px;
  }
  .services__bullet { color: var(--gold); margin-right: 3px; }

  .brand {
    position: absolute;
    left: 140px; top: 70px;
    display: flex; align-items: center; gap: 18px;
  }
  .brand__mark {
    width: 64px; height: 64px; border-radius: 50%;
    background: var(--gold);
  }
  .brand__name {
    font-family: "Cabin", Arial, sans-serif;
    font-weight: 600;
    font-size: 40px;
    color: var(--ink);
    letter-spacing: .5px;
  }
  .tagline {
    position: absolute;
    left: 222px; top: 138px;
    font-family: "Cabin", Arial, sans-serif;
    font-style: italic; font-weight: 700;
    font-size: 19px;
    color: var(--gold);
    letter-spacing: .5px;
  }
  .person {
    position: absolute; left: 56px; top: 300px;
  }
  .person__name {
    font-weight: 700; font-variant: small-caps;
    font-size: 19px; color: var(--text-light); letter-spacing: .8px;
  }
  .person__title { font-size: 14px; color: var(--gold); margin-top: 6px; }
  .details {
    position: absolute; left: 468px; top: 300px;
    font-size: 14px; line-height: 22px; color: var(--gold);
  }
  .details__contacts { margin-top: 16px; }
  .details__label { color: var(--text-light); display: inline-block; width: 22px; }
  .details__web { color: var(--text-light); font-weight: 700; }
</style>
</head>
<body>

  <section class="card card--services" aria-label="Business card reverse">
    <svg class="card__art" width="800" height="457" viewBox="0 0 800 457" aria-hidden="true">
      <path d="M0 132 Q400 70 800 132 L800 352 Q400 414 0 352 Z" fill="var(--band)"/>
      <path d="M0 126 Q400 62 800 126" fill="none" stroke="var(--gold)" stroke-width="3"/>
      <path d="M0 358 Q400 422 800 358" fill="none" stroke="var(--gold)" stroke-width="3"/>
      <path d="M0 138 Q400 80 800 138" fill="none" stroke="var(--gold-soft)" stroke-width="1"/>
      <path d="M0 346 Q400 404 800 346" fill="none" stroke="var(--gold-soft)" stroke-width="1"/>
    </svg>
    <div class="services">
      <p>We can help you:</p>
      <p><span class="services__bullet">•</span>Afford college while protecting retirement</p>
      <p><span class="services__bullet">•</span>Lower the total cost of college</p>
      <p><span class="services__bullet">•</span>Maximize financial aid qualification</p>
      <p><span class="services__bullet">•</span>Compare the net cost of public vs private schools</p>
    </div>
  </section>

  <section class="card card--contact" aria-label="Business card front">
    <svg class="card__art" width="800" height="457" viewBox="0 0 800 457" aria-hidden="true">
      <path d="M0 262 Q400 236 800 214 L800 457 L0 457 Z" fill="var(--ink)"/>
      <path d="M0 254 Q400 226 800 204" fill="none" stroke="var(--gold)" stroke-width="4"/>
      <path d="M0 246 Q400 220 800 196" fill="none" stroke="var(--gold-soft)" stroke-width="1.2"/>
    </svg>
    <div class="brand">
      <span class="brand__mark"></span>
      <span class="brand__name">Bright Harbor Advising</span>
    </div>
    <p class="tagline">PLAN WISELY, GRADUATE WITH EASE</p>

    <div class="person">
      <p class="person__name">Milo Trenholt</p>
      <p class="person__title">Certified College Planning Specialist</p>
    </div>
    <div class="details">
      <p>4870 Quarlow Lane</p>
      <p>Pellham Ridge, Idaho 58246</p>
      <div class="details__contacts">
        <p><span class="details__label">P:</span>701-555-0148</p>
        <p><span class="details__label">F:</span>866-555-0192</p>
        <p><span class="details__label">E:</span>milo@brightharboradvising.example</p>
        <p class="details__web">www.brightharboradvising.example</p>
      </div>
    </div>
  </section>

</body>
</html>
```